VELMO business card - High end Italian floors and coverings

We need a new design for our business card. We are an exclusive company located in Mexico.
Our commercial name is VELMO. Our legal name is Bruma Ceniza SA de CV.
We bring the latest trends in materials for floors and walls such as natural stones, wood, leather, design porcelanato tiles and so.
Our company image colors are black, white and red.
Our customers are high end architects and designers.
We are looking for an elegant but fresh design which reflects exclusivity, simplicity and reliability.
(we are working also in a new website)

Requirements
Nice to have
• back and front design
Space for 2 addresses (one for each showroom location)

```html
<!DOCTYPE html>
<html lang="es">
<head>
<meta charset="utf-8">
<title>VELMO – tarjeta de presentación</title>
<link rel="stylesheet" href="https://fonts.googleapis.com/css2?family=Open+Sans:wght@400&display=swap">
<style>
  :root {
    --red: #cc0000;
    --pink: #f4c6ca;
    --pink-deep: #e8a0a6;
    --white: #ffffff;
    --ink: #222222;
    --stage: #ecebe8;
    --card-w: 640px;
    --card-h: 366px;
  }
  * { box-sizing: border-box; margin: 0; padding: 0; }
  html, body { width: 1200px; height: 1000px; overflow: hidden; }
  body {
    background: var(--stage);
    font-family: "Open Sans", Arial, sans-serif;
    position: relative;
  }
  .card {
    position: absolute;
    left: 280px;
    width: var(--card-w);
    height: var(--card-h);
    overflow: hidden;
    box-shadow: 0 6px 18px rgba(0,0,0,.18);
  }

  /* Back: brand side */
  .card--brand { top: 90px; background: var(--red); }
  .brand__name, .brand__legal {
    position: absolute; right: 60px;
    font-family: "Open Sans", Arial, sans-serif; font-weight: 400;
    color: var(--white); text-align: right;
  }
  .brand__name { top: 120px; font-size: 44px; letter-spacing: 2px; line-height: 1; }
  .brand__legal { top: 178px; font-size: 13px; letter-spacing: 1px; }

  /* Front: contact side */
  .card--contact { top: 540px; background: var(--white); }
  .contact__rule {
    position: absolute; right: 0; top: 0;
    width: 250px; height: 7px; background: var(--red);
  }
  .contact__block {
    position: absolute; left: 28px; top: 28px;
    width: 120px; height: 80px; background: var(--pink);
  }
  .contact__block--small {
    left: 48px; top: 124px;
    width: 44px; height: 44px; background: var(--pink-deep);
  }
  .contact__name {
    position: absolute; left: 172px; top: 30px;
    color: var(--red); font-size: 30px; font-weight: 400; line-height: 1.1;
  }
  .contact__email {
    position: absolute; left: 174px; top: 72px;
    color: var(--ink); font-size: 13px;
  }
  .contact__band {
    position: absolute; left: 0; bottom: 0;
    width: 100%; height: 122px; background: var(--red);
    color: var(--white); font-size: 13px; line-height: 1.45;
  }
  .office { position: absolute; bottom: 20px; list-style: none; }
  .office--gdl { left: 28px; }
  .office--cdmx { right: 28px; }
  .office li { display: flex; align-items: center; gap: 7px; }
  .office .phone::before {
    content: ""; width: 9px; height: 9px; background: var(--white); display: inline-block;
  }
</style>
</head>
<body>

<section class="card card--brand" aria-label="Reverso de la tarjeta">
  <p class="brand__name">VELMO</p>
  <p class="brand__legal">Bruma Ceniza SA de CV</p>
</section>

<section class="card card--contact" aria-label="Frente de la tarjeta">
  <div class="contact__rule"></div>
  <div class="contact__block"></div>
  <div class="contact__block contact__block--small"></div>
  <h1 class="contact__name">Carla Ruiz Tenorio</h1>
  <p class="contact__email">carla@velmo.com.mx</p>
  <div class="contact__band">
    <ul class="office office--gdl">
      <li>Cedro 418 Col. Arboleda</li>
      <li>Guadalajara, Jal.</li>
      <li class="phone">(33) 2150 4471</li>
      <li class="phone">(33) 2468 1357</li>
    </ul>
    <ul class="office office--cdmx">
      <li>Lago Sereno 27 B</li>
      <li>Col. Ribera, Del.</li>
      <li>Miguel Hidalgo, Mexico D.F.</li>
      <li class="phone">(55) 4821 3390</li>
    </ul>
  </div>
</section>

</body>
</html>
```